Morvex Business Card (intended for Business Card sized magnet)

Hi guys,

I would like to get a design for my business card for the restaurant. The design must be single sided as I intend to produce business card sized magnets.

The File attached must me on and I'm open for new ides

Can you please ensure that the design meets Cardowell's magnetic business card size specifications:

http://www.cardowell.example.au/custom-magnets.aspx?txi=15695&xnid=TopNav_Magnetic+Business+Cards+(linked+item)_Magnets_Marketing+Products&xnav=TopNav

Full Bleed Size (starting document size):
90 x 52 mm
1062 x 615 pixels
* Finished artwork should use the full bleed dimensions for best results.

Document Trim Size (final size after being cut):
87 x 49 mm
1028 x 579 pixels
* Please be sure to keep all text within the safe margin.

Resolution:
300 DPI

The winning design/source files need to meet these specifications.

Thanks
Updates

Hi guys, can I see more options please Thanks

```html
<!DOCTYPE html>
<html lang="en">
<head>
<meta charset="utf-8">
<title>Morvex – Business Card</title>
<link rel="stylesheet" href="https://fonts.googleapis.com/css2?family=PT+Sans:wght@400&display=swap">
<style>
  :root {
    --page: #ffffff;
    --card-light: #d6e6f3;
    --card-mid: #8fbfe2;
    --card-deep: #1f80c5;
    --ink: #0a0a0a;
    --tile-border: rgba(200, 220, 240, 0.85);
    --icon-light: #fafafa;
    --icon-dark: #a9a9a9;
  }
  * { margin: 0; padding: 0; box-sizing: border-box; }
  html, body {
    width: 1200px; height: 542px; overflow: hidden;
    background: var(--page);
    font-family: "PT Sans", sans-serif;
    color: var(--ink);
  }
  .card {
    position: absolute; left: 239px; top: 0;
    width: 961px; height: 542px;
    background: linear-gradient(90deg, var(--card-light) 5%, var(--card-mid) 40%, var(--card-deep) 100%);
  }
  .brand {
    position: absolute; left: 717px; top: 12px;
    transform: translateX(-50%);
    font-size: 54px; line-height: 1; letter-spacing: 0.5px;
  }
  .dish {
    position: absolute;
    border: 2px solid var(--tile-border);
    opacity: 0.8;
  }
  .dish--falafel { left: 533px; top: 150px; width: 64px; height: 64px; background: linear-gradient(135deg, #c9c7b8, #8f7f5c); }
  .dish--grill   { left: 621px; top: 148px; width: 69px; height: 69px; background: linear-gradient(135deg, #5a4a42, #b0584a); }
  .dish--platter { left: 699px; top: 150px; width: 65px; height: 65px; background: linear-gradient(135deg, #7f8fa0, #5c6a7a); }
  .dish--drink   { left: 781px; top: 147px; width: 65px; height: 69px; background: linear-gradient(160deg, #4f5a63, #b9c9a8); }
  .dish--dessert { left: 866px; top: 148px; width: 66px; height: 67px; background: linear-gradient(135deg, #7b8fa6, #9a6f8a); }

  .address {
    position: absolute; left: 252px; top: 266px;
    font-size: 20.5px;
  }
  .contact { position: absolute; left: 264px; top: 314px; list-style: none; }
  .contact__item {
    display: flex; align-items: center;
    height: 30px; margin-bottom: 24.5px;
    font-size: 20.5px;
  }
  .contact__icon { width: 31px; height: 31px; margin-right: 14px; flex: none; }
</style>
</head>
<body>
  <main class="card">
    <div class="brand">Morvex</div>

    <div class="dish dish--falafel" role="img" aria-label="Photo of falafel on a plate"></div>
    <div class="dish dish--grill" role="img" aria-label="Photo of grilled skewers"></div>
    <div class="dish dish--platter" role="img" aria-label="Photo of a mezze platter"></div>
    <div class="dish dish--drink" role="img" aria-label="Photo of a mint lemonade"></div>
    <div class="dish dish--dessert" role="img" aria-label="Photo of ice cream dessert"></div>

    <p class="address">412Brook hollow rd,ashdale north 3170</p>

    <svg width="0" height="0" style="position:absolute">
      <defs>
        <radialGradient id="button" cx="40%" cy="30%" r="75%">
          <stop offset="0" stop-color="var(--icon-light)"/>
          <stop offset="1" stop-color="var(--icon-dark)"/>
        </radialGradient>
      </defs>
    </svg>

    <ul class="contact">
      <li class="contact__item">
        <svg class="contact__icon" viewBox="0 0 32 32" aria-hidden="true">
          <circle cx="16" cy="16" r="15" fill="url(#button)" stroke="#8a8a8a"/>
          <rect x="12" y="8" width="8" height="16" rx="2" fill="#111"/>
          <rect x="13.5" y="10" width="5" height="5" fill="#ddd"/>
        </svg>
        0355501234
      </li>
      <li class="contact__item">
        <svg class="contact__icon" viewBox="0 0 32 32" aria-hidden="true">
          <circle cx="16" cy="16" r="15" fill="url(#button)" stroke="#8a8a8a"/>
          <path d="M8 16 L16 9 L24 16 L22 16 L22 23 L10 23 L10 16 Z" fill="#111"/>
          <rect x="14" y="18" width="4" height="5" fill="#ddd"/>
        </svg>
        www.morvex.com.au
      </li>
      <li class="contact__item">
        <svg class="contact__icon" viewBox="0 0 32 32" aria-hidden="true">
          <circle cx="16" cy="16" r="15" fill="url(#button)" stroke="#8a8a8a"/>
          <rect x="8" y="11" width="16" height="11" fill="#111"/>
          <path d="M9 12 L16 18 L23 12" fill="none" stroke="#ddd" stroke-width="1.5"/>
        </svg>
        Morvex412@mailbox.example
      </li>
    </ul>
  </main>
</body>
</html>
```